Update Law Firm Website

Update law firm website pages, add pages for employees. Current website looks stale. www.lowrevanlaw.com

Target Market(s)

Personal injury clients

Industry/Entity Type

Legal

Number of Pages Required

5+ page

Font styles to use
Serif

Requirements
Must have
• User friendly and engaging design
Nice to have
• ?
Should not have
• scales of justice, law books,

```html
<!DOCTYPE html>
<html lang="en">
<head>
<meta charset="utf-8">
<title>Keystone Injury Law Group</title>
<link href="https://fonts.googleapis.com/css2?family=Libre+Baskerville:wght@700&family=Nunito:wght@400;600;700&family=Open+Sans:ital,wght@0,400;0,600;0,700;1,400;1,700&display=swap" rel="stylesheet">
<style>
:root{
  --maroon:#6b0a0a;
  --maroon-deep:#520606;
  --gold:#e6ac2c;
  --gold-dark:#c98f14;
  --ink:#333;
  --muted:#666;
  --light:#eef0f0;
  --white:#fff;
}
*{box-sizing:border-box;margin:0;padding:0}
html,body{width:1200px;height:3243px;overflow:hidden}
body{font-family:"Open Sans",Arial,sans-serif;color:var(--ink);background:var(--white);position:relative}
.container{width:900px;margin:0 auto;position:relative}

/* top bar */
.topbar{height:58px;background:var(--maroon)}
.topbar .container{height:58px}
.brand{position:absolute;left:0;top:12px}
.brand-name{font-family:"Libre Baskerville",Georgia,serif;font-weight:700;color:var(--white);font-size:16px;letter-spacing:.5px}
.brand-sub{font-family:"Libre Baskerville",Georgia,serif;font-weight:700;color:var(--gold);font-size:10px;margin-top:3px;letter-spacing:.3px}
.consult{position:absolute;right:20px;top:7px;color:var(--white);text-align:left}
.consult small{display:block;font-size:13px;margin-left:22px}
.consult strong{display:flex;align-items:center;gap:6px;font-style:italic;font-size:21px}

/* nav */
.nav{height:50px;border-bottom:1px solid #ddd}
.nav ul{list-style:none;display:flex;gap:18px;height:50px;align-items:center;font-size:12.5px;font-weight:600;color:#222}
.nav li.active{color:var(--gold-dark)}
.nav .search{margin-left:18px}

/* hero */
.hero{height:508px;position:relative;background:linear-gradient(100deg,#7b7f78 0%,#9ea29a 35%,#6f6d66 60%,#3d3a36 100%);border-bottom:6px solid var(--maroon)}
.hero-copy{position:absolute;left:592px;top:262px;color:var(--white)}
.hero-copy .kicker{font-size:28px;letter-spacing:.5px}
.hero-copy h1{font-size:37px;font-weight:700;letter-spacing:1px;line-height:1.1}
.hero-copy p{font-size:13px;margin-top:6px}
.btn{display:inline-block;background:var(--gold);color:var(--white);font-weight:600;font-size:14px;text-align:center}
.hero .btn{margin-top:20px;width:160px;line-height:40px;border:2px solid #f3c55c}

/* practice */
.practice{height:461px;background:var(--light);text-align:center;padding-top:50px}
.section-title{font-family:"Nunito",Arial,sans-serif;font-weight:600;font-size:27px;color:#222}
.section-sub{font-size:12.5px;color:var(--muted);margin-top:4px}
.cards{display:flex;gap:22px;margin-top:28px}
.card{width:208px;height:266px;background:var(--white);box-shadow:0 3px 6px rgba(0,0,0,.25)}
.card h3{background:var(--maroon);color:var(--white);height:60px;display:flex;align-items:center;justify-content:center;font-size:12.5px;font-weight:700;letter-spacing:1px;line-height:1.3}
.card svg{margin:20px auto 10px;display:block}
.card p{font-size:11px;color:var(--muted);line-height:1.55;padding:0 24px}
.card a{display:block;margin-top:6px;font-size:12px;font-style:italic;font-weight:700;color:var(--maroon);text-decoration:underline}
.arrow{position:absolute;top:190px}
.arrow.prev{left:-48px}.arrow.next{right:-40px}

/* advocate */
.advocate{height:361px;padding-top:52px}
.portrait{float:left;width:173px;height:191px;border:2px solid #bbb;padding:4px;background:#fff;margin:6px 45px 6px 12px}
.portrait div{width:100%;height:100%;background:linear-gradient(160deg,#5a5f66,#2b2e33)}
.advocate h2{font-family:"Nunito",Arial,sans-serif;font-weight:700;font-size:25px;color:#222}
.advocate p{font-size:12px;line-height:1.6;color:var(--muted);text-align:justify}
.advocate .lead{margin-top:12px}
.advocate .more{margin-top:14px}
.skyline{height:179px;background:linear-gradient(180deg,#e7d4b8 0%,#b9a58a 45%,#6b6258 100%)}

/* testimonials */
.testimonials{height:323px;background:linear-gradient(180deg,#7a1414,#5a0909);text-align:center;padding-top:40px;color:var(--white)}
.testimonials .section-title{color:var(--white)}
.testimonials .section-sub{color:#eed}
.quotes{display:flex;gap:38px;margin-top:28px}
.quote{width:441px;height:130px;background:#f1eeee;padding:8px;text-align:left}
.quote div{border:1px solid #c99;height:100%;padding:14px 24px;position:relative;font-size:12.5px;font-style:italic;color:#555;line-height:1.45}
.quote b{color:var(--gold);font-size:24px;position:absolute;left:20px;top:6px;font-style:normal}
.quote span{padding-left:18px;display:block}
.quote em{position:absolute;right:24px;bottom:10px;color:var(--gold-dark)}
.dots{margin-top:22px;display:flex;justify-content:center;gap:8px}
.dots i{width:14px;height:14px;border-radius:50%;border:2px solid #fff}
.dots i.on{background:#fff}

/* liability + form */
.liability{height:640px;padding-top:70px}
.liability .container{width:950px}
.basis{width:452px}
.basis h2{font-family:"Nunito",Arial,sans-serif;font-weight:600;font-size:26px;color:#222}
.basis .intro{font-size:12.5px;color:var(--muted);line-height:1.6;margin:14px 0 20px}
.acc{height:50px;border:1px solid #ddd;box-shadow:0 1px 3px rgba(0,0,0,.15);margin-bottom:13px;display:flex;align-items:center;justify-content:space-between;padding:0 22px;font-size:13px;letter-spacing:.5px;color:#444}
.acc.open{background:var(--gold);color:var(--white);border-color:var(--gold);font-weight:600}
.basis .body{font-size:12.2px;color:var(--muted);line-height:1.6;text-align:justify;margin-top:22px}
.contact{position:absolute;right:0;top:-10px;width:433px;height:487px;background:var(--maroon);padding:26px 26px;border:4px solid #7e1616}
.contact label{display:block;color:var(--white);font-size:12.5px;font-weight:700;letter-spacing:.5px;margin:8px 0 10px}
.field{height:44px;background:var(--white);margin-bottom:18px}
.field.tall{height:106px}
.contact .btn{display:block;width:147px;line-height:36px;margin:14px auto 0}

/* map */
.map{height:350px;position:relative;background:linear-gradient(120deg,#e8e4d8 0%,#dfe6cf 45%,#d9dccf 70%,#a9cbe8 85%,#9cc3e6 100%)}
.address{position:absolute;left:134px;top:83px;width:259px;height:234px;background:var(--gold);color:var(--white);padding:22px 28px;font-size:13px;font-style:italic;font-weight:600}
.address h4{font-size:15px;font-style:normal;text-decoration:underline;margin-bottom:10px}
.address p{display:flex;gap:8px;margin-bottom:16px;line-height:1.45}

/* footer */
.footer{height:313px;background:var(--maroon-deep);color:var(--white);position:relative}
.footer .cols{position:absolute;top:36px;left:147px;display:flex}
.footer h5{font-size:14px;font-weight:700;letter-spacing:.5px;margin-bottom:10px}
.footer ul{list-style:none;font-size:11px;line-height:1.6}
.footer li::before{content:"› "}
.col-areas{width:355px;display:flex;flex-wrap:wrap}
.col-areas h5{width:100%}
.col-areas ul{width:150px}
.col-blog{width:261px}
.col-blog li{text-decoration:underline;font-style:italic}
.badge{position:absolute;left:934px;top:136px;width:121px;height:41px;background:#f4f0e4;border:3px solid #d8a21d}
.legal{position:absolute;left:153px;top:270px;font-size:10.5px;color:#d9a0a0;line-height:1.6}
</style>
</head>
<body>

<header class="topbar">
  <div class="container">
    <div class="brand">
      <div class="brand-name">KEYSTONE INJURY LAW GROUP</div>
      <div class="brand-sub">DANIEL R. MARSH, ESQUIRE</div>
    </div>
    <div class="consult">
      <small>Free Consultation</small>
      <strong><svg width="16" height="16" viewBox="0 0 24 24"><path fill="#fff" d="M6.6 10.8a15.1 15.1 0 0 0 6.6 6.6l2.2-2.2c.3-.3.7-.4 1-.2 1.1.4 2.3.6 3.6.6.6 0 1 .4 1 1V20c0 .6-.4 1-1 1A17 17 0 0 1 3 4c0-.6.4-1 1-1h3.5c.6 0 1 .4 1 1 0 1.300.2 2.5.6 3.6.1.3 0 .7-.2 1z"/></svg>(555) 014-2200</strong>
    </div>
  </div>
</header>

<nav class="nav">
  <div class="container">
    <ul>
      <li class="active">SLIP AND FALL</li><li>AUTO ACCIDENT</li><li>CONSTRUCTION INJURIES</li><li>MEDICAL MALPRACTICE</li><li>RESULTS</li><li>ABOUT US</li><li>CONTACT US</li>
      <li class="search"><svg width="16" height="16" viewBox="0 0 24 24"><circle cx="10" cy="10" r="6.5" fill="none" stroke="#222" stroke-width="3"/><path d="M15 15l6 6" stroke="#222" stroke-width="3"/></svg></li>
    </ul>
  </div>
</nav>

<section class="hero">
  <div role="img" aria-label="Photo of an injured woman on the phone beside a police officer at a car accident scene" style="position:absolute;inset:0"></div>
  <div class="hero-copy">
    <div class="kicker">EVERY INJURED CLIENTS DESERVES</div>
    <h1>POWERFULL REPRESENTATION</h1>
    <p>It is a long established fact that a reader will be distracted by the readable content of a page</p>
    <span class="btn">CONTACT US</span>
  </div>
</section>

<section class="practice">
  <div class="container">
    <h2 class="section-title">Our Area of Practice</h2>
    <p class="section-sub">It is a long established fact that a reader will be distracted content</p>
    <svg class="arrow prev" width="20" height="32" viewBox="0 0 20 32"><path d="M16 2 4 16l12 14" fill="none" stroke="#333" stroke-width="3"/></svg>
    <svg class="arrow next" width="20" height="32" viewBox="0 0 20 32"><path d="M4 2l12 14L4 30" fill="none" stroke="#333" stroke-width="3"/></svg>
    <div class="cards">
      <div class="card">
        <h3>TRACTOR-TRAILER<br>COLLISIONS</h3>
        <svg width="80" height="56" viewBox="0 0 80 56"><rect x="30" y="10" width="26" height="24" fill="none" stroke="#e6ac2c" stroke-width="4"/><rect x="12" y="22" width="54" height="16" fill="#e6ac2c"/><circle cx="22" cy="44" r="9" fill="#fff" stroke="#e6ac2c" stroke-width="4"/><circle cx="56" cy="44" r="9" fill="#fff" stroke="#e6ac2c" stroke-width="4"/></svg>
        <p>It is a long established fact that a reader will be distracted by the readable content.</p>
        <a>Learn More+</a>
      </div>
      <div class="card">
        <h3>MOTORCYCLE<br>CRASHES</h3>
        <svg width="80" height="56" viewBox="0 0 80 56"><circle cx="14" cy="42" r="9" fill="none" stroke="#e6ac2c" stroke-width="4"/><circle cx="38" cy="42" r="9" fill="none" stroke="#e6ac2c" stroke-width="4"/><path d="M14 42l10-16h14l0 16" fill="none" stroke="#e6ac2c" stroke-width="4"/><rect x="48" y="22" width="28" height="22" fill="#e6ac2c"/></svg>
        <p>It is a long established fact that a reader will be distracted by the readable content.</p>
        <a>Learn More+</a>
      </div>
      <div class="card">
        <h3>CONSTRUCTION<br>ACCIDENTS</h3>
        <svg width="80" height="56" viewBox="0 0 80 56"><path d="M30 54 44 2M52 54 66 2M34 40h22M38 26h22M42 12h22" fill="none" stroke="#e6ac2c" stroke-width="4"/></svg>
        <p>It is a long established fact that a reader will be distracted by the readable content.</p>
        <a>Learn More+</a>
      </div>
      <div class="card">
        <h3>MEDICAL<br>MALPRACTICE</h3>
        <svg width="80" height="56" viewBox="0 0 80 56"><rect x="14" y="12" width="52" height="42" rx="6" fill="#e6ac2c"/><rect x="30" y="4" width="20" height="10" rx="3" fill="none" stroke="#e6ac2c" stroke-width="4"/><path d="M40 22v24M28 34h24" stroke="#fff" stroke-width="7"/></svg>
        <p>It is a long established fact that a reader will be distracted by the readable content.</p>
        <a>Learn More+</a>
      </div>
    </div>
  </div>
</section>

<section class="advocate">
  <div class="container">
    <div class="portrait"><div role="img" aria-label="Portrait photo of the firm's lead attorney in a dark suit"></div></div>
    <h2>Legal Advocate for Your Injury Claim</h2>
    <p class="lead">When you are hit by a fatigued driver of a tractor-trailer or you suffer a fatal stroke because of a delayed diagnosis by a physician, the consequences can include staggering medical bills, debilitating pain and permanent disability. While overcoming the emotional, physical and financial hardships associated with a serious injury always present serious challenges, incidents resulting in substantial injuries can be even more traumatic when they are caused by the negligent, reckless or intentional actions of another individual, company or government entity.</p>
    <p class="more">Keystone personal injury lawyer Daniel Marsh recognizes that victims of distracted drivers, inattentive property owners and substandard medical providers might not focus on financial compensation as their first priority. However, injury victims must eventually confront the medical bills, lost income and expenses associated with maintaining a high quality of life after suffering a significant injury. Our personal injury law firm aggressively pursues full recovery for our clients by anticipating and effectively responding to insurance company tactics designed to minimize or prevent recovery. Mr. Marsh is an experienced former insurance defense attorney who fully exploits his insider's knowledge when dealing with insurance companies.</p>
  </div>
</section>
<div class="skyline" role="img" aria-label="Photo of a city skyline at sunset"></div>

<section class="testimonials">
  <div class="container">
    <h2 class="section-title">Our Happy Clients Say</h2>
    <p class="section-sub">It is a long established fact that a reader will be distracted content</p>
    <div class="quotes">
      <div class="quote"><div><b>“</b><span>It is a long established fact that a reader will be distracted by the readable content.It is a long established fact that a reader will be distracted by the readable content.</span><em>- J.O.</em></div></div>
      <div class="quote"><div><b>“</b><span>It is a long established fact that a reader will be distracted by the readable content.It is a long established fact that a reader will be distracted by the readable content.</span><em>- J.O.</em></div></div>
    </div>
    <div class="dots"><i class="on"></i><i></i></div>
  </div>
</section>

<section class="liability">
  <div class="container">
    <div class="basis">
      <h2>Basis for Imposing Liability</h2>
      <p class="intro">The basis for imposing liability for damages in a personal injury lawsuit may be negligence, recklessness, intentional misconduct or strict liability.</p>
      <div class="acc">NEGLIGENCE &amp; RECKLESSNESS <svg width="16" height="16" viewBox="0 0 16 16"><circle cx="8" cy="8" r="7" fill="none" stroke="#e6ac2c" stroke-width="1.5"/><path d="M8 4v8M4 8h8" stroke="#e6ac2c" stroke-width="1.5"/></svg></div>
      <div class="acc">INTENTIONAL ACTIONS <svg width="16" height="16" viewBox="0 0 16 16"><circle cx="8" cy="8" r="7" fill="none" stroke="#e6ac2c" stroke-width="1.5"/><path d="M8 4v8M4 8h8" stroke="#e6ac2c" stroke-width="1.5"/></svg></div>
      <div class="acc open">STRICT LIABILITY <svg width="20" height="20" viewBox="0 0 20 20"><circle cx="10" cy="10" r="9" fill="#fff"/><path d="M5 10h10" stroke="#e6ac2c" stroke-width="2"/></svg></div>
      <p class="body">There are certain cases where an injury victim does not have to specifically prove any of the forms of misconduct indicated above. When a defective product causes injury to a consumer, for example, any party involved in the production or distribution chain for the product can be liable without the injury victim being required to prove the specific substandard conduct that caused the defect. Similarly, when a person violates a public safety law like a leash law or a traffic safety law, such as the requirement to stop at a red light, this might constitute "negligence per se." While negligence can be established by such a violation, this does not relieve the injury victim of the obligation to demonstrate that the violation caused the victim's injuries.</p>
    </div>
    <form class="contact">
      <label>FULL NAME</label><div class="field"></div>
      <label>EMAIL ADDRESS</label><div class="field"></div>
      <label>PHONE NUMBER</label><div class="field"></div>
      <label>YOUR MESSAGE</label><div class="field tall"></div>
      <span class="btn">Submit</span>
    </form>
  </div>
</section>

<section class="map">
  <div role="img" aria-label="Road map of the region around the office" style="position:absolute;inset:0"></div>
  <div class="address">
    <h4>Our Address</h4>
    <p><svg width="12" height="16" viewBox="0 0 12 16"><path d="M6 0a6 6 0 0 0-6 6c0 4.5 6 10 6 10s6-5.5 6-10a6 6 0 0 0-6-6zm0 8.5A2.5 2.5 0 1 1 6 3.5a2.5 2.5 0 0 1 0 5z" fill="#fff"/></svg><span>820 Harbor Ave #310<br>Riverton, PA 19000</span></p>
    <p><svg width="14" height="14" viewBox="0 0 24 24"><path fill="#fff" d="M6.6 10.8a15.1 15.1 0 0 0 6.6 6.6l2.2-2.2c.3-.3.7-.4 1-.2 1.1.4 2.3.6 3.6.6.6 0 1 .4 1 1V20c0 .6-.4 1-1 1A17 17 0 0 1 3 4c0-.6.4-1 1-1h3.5c.6 0 1 .4 1 1 0 1.3.2 2.5.6 3.6.1.3 0 .7-.2 1z"/></svg>(555) 014-2200</p>
    <p><svg width="14" height="12" viewBox="0 0 14 12"><rect width="14" height="12" rx="1" fill="#fff"/><path d="M0 1l7 5 7-5" fill="none" stroke="#e6ac2c" stroke-width="1.5"/></svg>www.keystoneinjurygroup.com</p>
  </div>
</section>

<footer class="footer">
  <div class="cols">
    <div class="col-areas">
      <h5>PRACTICE AREAS</h5>
      <ul><li>Tractor-trailer collisions</li><li>Motorcycle crashes</li><li>Construction accidents</li><li>Medical malpractice</li><li>Defective products</li><li>Pipeline explosions</li><li>Dog bites</li><li>Car accidents</li></ul>
      <ul><li>Pedestrian struck by motor vehicles</li><li>Bicycle auto collisions</li><li>Wrongful death cases</li><li>Premises liability</li><li>Slip and fall (trip and fall)</li></ul>
    </div>
    <div class="col-blog">
      <h5>RECENT BLOG</h5>
      <ul><li>Lorem ipsum is a demo text</li><li>Lorem ipsum is a demo text</li><li>Lorem ipsum is a demo text use it design purpose</li><li>Lorem ipsum is a demo text</li><li>Lorem ipsum is a demo text</li></ul>
    </div>
    <div>
      <h5>OUR SITELINKS</h5>
      <ul><li>Slip and Fall</li><li>Auto Accident</li><li>Construction Injuries</li><li>Medical Practice</li><li>Results</li><li>About us</li><li>Contact Us</li></ul>
    </div>
  </div>
  <div class="badge"></div>
  <p class="legal">© 2016. All rights reserved. You are not establishing an attorney-client relationship by reviewing this website or by contacting us.<br>An attorney-client relationship is not established until you receive a signed agreement letter from the firm</p>
</footer>

</body>
</html>
```